Design a double sided business card

We are looking for a clean, eye-catching, and contemporary design that enhances the brand and presents a premium, professional image. Our preference is for a brown card with black gloss detailing and embossed elements; however, we are open to creative input and design suggestions that best achieve a strong visual impact.

Please see the attached existing business card for reference. We use both black and brown colours consistently across our branding.

On sample provided

```html
<!DOCTYPE html>
<html lang="en">
<head>
<meta charset="utf-8">
<title>Korvane business card – front and back</title>
<link rel="stylesheet" href="https://fonts.googleapis.com/css2?family=Montserrat:wght@500;700;800&family=Arimo:wght@400&display=swap">
<style>
  :root {
    --stage: #2a2b2e;
    --sand: #cdb99d;
    --sand-deep: #c1ab8c;
    --sand-line: #bba485;
    --ink: #141414;
    --night: #111112;
    --night-soft: #1e1e20;
    --gold: #cdb99d;
  }
  html, body {
    margin: 0;
    width: 1200px;
    height: 900px;
    overflow: hidden;
    background: var(--stage);
  }
  .canvas {
    position: relative;
    width: 1200px;
    height: 900px;
  }
  .card {
    position: absolute;
    width: 600px;
    height: 343px;
    border-radius: 4px;
    overflow: hidden;
    box-shadow: 0 18px 40px rgba(0,0,0,.45);
  }

  /* Front */
  .card-front {
    left: 110px;
    top: 80px;
    background: var(--sand);
    color: var(--ink);
    font-family: "Arimo", Arial, sans-serif;
  }
  .holder {
    position: absolute;
    right: 34px;
    top: 28px;
    text-align: right;
    font-family: "Montserrat", sans-serif;
  }
  .holder-name {
    margin: 0;
    font-size: 25px;
    font-weight: 800;
    letter-spacing: .5px;
  }
  .holder-role {
    margin: 2px 0 0;
    font-size: 11px;
    font-weight: 500;
    letter-spacing: 4.5px;
  }
  .backdrop-mark {
    position: absolute;
    right: 70px;
    top: 96px;
    width: 150px;
    height: 150px;
    background: var(--sand-deep);
    border: 6px solid var(--sand-line);
    box-sizing: border-box;
  }
  .brand {
    position: absolute;
    left: 40px;
    top: 104px;
    display: flex;
    align-items: center;
    gap: 14px;
  }
  .brand-square {
    width: 46px;
    height: 46px;
    border: 5px solid var(--ink);
    box-sizing: border-box;
  }
  .brand-name {
    font-family: "Montserrat", sans-serif;
    font-weight: 800;
    font-size: 26px;
    letter-spacing: 5px;
  }
  .contacts {
    position: absolute;
    left: 40px;
    top: 200px;
    margin: 0;
    padding: 0;
    list-style: none;
    font-size: 15px;
    line-height: 22px;
  }
  .contacts li {
    display: flex;
    align-items: flex-start;
    gap: 10px;
  }
  .contacts svg {
    flex: none;
    width: 14px;
    height: 14px;
    margin-top: 4px;
    fill: var(--ink);
  }

  /* Back */
  .card-back {
    left: 490px;
    top: 477px;
    background: var(--night);
  }
  .back-texture {
    position: absolute;
    inset: 0;
    background: linear-gradient(135deg, var(--night-soft) 0%, var(--night) 55%, #19191b 100%);
  }
  .back-brand {
    position: absolute;
    left: 250px;
    top: 200px;
    display: flex;
    align-items: center;
    gap: 16px;
  }
  .back-brand .brand-square {
    width: 54px;
    height: 54px;
    border-color: var(--gold);
  }
  .back-brand .brand-name {
    color: var(--gold);
    font-size: 30px;
  }
</style>
</head>
<body>
<main class="canvas">

  <section class="card card-front" aria-label="Card front">
    <header class="holder">
      <h1 class="holder-name">RAVI MEHTA</h1>
      <p class="holder-role">DIRECTOR</p>
    </header>

    <div class="backdrop-mark" aria-hidden="true"></div>

    <div class="brand">
      <span class="brand-square" aria-hidden="true"></span>
      <span class="brand-name">KORVANE</span>
    </div>

    <ul class="contacts">
      <li>
        <svg viewBox="0 0 16 16" aria-hidden="true"><path d="M3 1h3l1.5 4-2 1.3a8.5 8.5 0 0 0 4.2 4.2L11 8.5l4 1.5v3a2 2 0 0 1-2 2A12 12 0 0 1 1 3a2 2 0 0 1 2-2z"/></svg>
        <span>0800 214 6037</span>
      </li>
      <li>
        <svg viewBox="0 0 16 16" aria-hidden="true"><path d="M4 0h8a1.5 1.5 0 0 1 1.5 1.5v13A1.5 1.5 0 0 1 12 16H4a1.5 1.5 0 0 1-1.5-1.5v-13A1.5 1.5 0 0 1 4 0zm0 2v10.5h8V2z"/></svg>
        <span>0791 482 3506</span>
      </li>
      <li>
        <svg viewBox="0 0 16 16" aria-hidden="true"><path d="M1 3h14v10H1zm1.5 1.5L8 9l5.5-4.5v-.1H2.5z"/></svg>
        <span>ravi@korvane.co.uk</span>
      </li>
      <li>
        <svg viewBox="0 0 16 16" aria-hidden="true"><path d="M8 0a8 8 0 1 0 0 16A8 8 0 0 0 8 0zm5.9 7h-2.6a12 12 0 0 0-1.1-4.7A6 6 0 0 1 13.9 7zM8 2c.8 1 1.5 2.8 1.6 5H6.4C6.5 4.8 7.2 3 8 2zM5.8 2.3A12 12 0 0 0 4.7 7H2.1a6 6 0 0 1 3.7-4.7zM2.1 9h2.6a12 12 0 0 0 1.1 4.7A6 6 0 0 1 2.1 9zM8 14c-.8-1-1.5-2.8-1.6-5h3.2c-.1 2.2-.8 4-1.6 5zm2.2-.3A12 12 0 0 0 11.3 9h2.6a6 6 0 0 1-3.7 4.7z"/></svg>
        <span>www.korvane.co.uk</span>
      </li>
      <li>
        <svg viewBox="0 0 16 16" aria-hidden="true"><path d="M8 0a5.5 5.5 0 0 0-5.5 5.5C2.5 10 8 16 8 16s5.5-6 5.5-10.5A5.5 5.5 0 0 0 8 0zm0 8a2.5 2.5 0 1 1 0-5 2.5 2.5 0 0 1 0 5z"/></svg>
        <span>14 Millbrook Yard<br>Harlow CM17 4RT</span>
      </li>
    </ul>
  </section>

  <section class="card card-back" aria-label="Card back">
    <div class="back-texture" role="img" aria-label="Embossed gloss-black repeating brand pattern across the card"></div>
    <div class="back-brand">
      <span class="brand-square" aria-hidden="true"></span>
      <span class="brand-name">KORVANE</span>
    </div>
  </section>

</main>
</body>
</html>
```